Executive recruiting firm in need of business card design

Executive recruiting firm looking for a sleek, classy and modern business card design; card itself will be square shape, rounded edges and soft touch paper, our colors are dark blues in the navy color scale, silvers and grays. Reference our website for a better idea of our company's feel and goals at Staffvex.com - our company message is "Employee Engagement Begins at Recruitment" this should be on the card

Industry/Entity Type

Business

```html
<!DOCTYPE html>
<html lang="en">
<head>
<meta charset="utf-8">
<title>Staffvex Business Cards</title>
<link rel="stylesheet" href="https://fonts.googleapis.com/css2?family=Arimo:wght@400;700&display=swap">
<style>
  :root {
    --navy: #1c1f5a;
    --sky: #3a9fd0;
    --paper: #f6f7f8;
    --ink: #1e1e28;
    --stage: #3a3a3d;
  }
  * { box-sizing: border-box; margin: 0; padding: 0; }
  html, body { width: 1200px; height: 997px; overflow: hidden; }
  body {
    background: var(--stage);
    font-family: "Arimo", Arial, sans-serif;
    position: relative;
  }
  .card {
    position: absolute;
    width: 540px;
    height: 310px;
    background: var(--paper);
    border-radius: 4px;
    overflow: hidden;
    box-shadow: 0 10px 30px rgba(0,0,0,.45);
  }
  .card--back { left: 45px; top: 340px; }
  .card--front { left: 615px; top: 340px; }

  .brand-name {
    position: absolute;
    font-family: "Arimo", Arial, sans-serif;
    font-weight: 700;
    font-size: 40px;
    color: var(--navy);
    line-height: 1;
  }

  /* back */
  .card--back .brand-name { left: 0; right: 0; top: 96px; text-align: center; }
  .card--back .rule { position: absolute; left: 0; right: 0; top: 226px; height: 4px; background: var(--navy); }
  .card--back .band {
    position: absolute; left: 0; right: 0; top: 236px; height: 40px;
    background: var(--navy); color: #fff;
    display: flex; align-items: center; justify-content: center;
    font-weight: 700; font-size: 14px; letter-spacing: 1px;
  }

  /* front */
  .card--front .brand-name { left: 150px; top: 50px; font-size: 36px; }
  .card--front .top-rule { position: absolute; left: 150px; right: 30px; top: 108px; height: 1px; background: var(--sky); }
  .person { position: absolute; left: 30px; top: 146px; }
  .person__name { font-weight: 700; font-size: 19px; color: var(--navy); letter-spacing: .5px; }
  .person__role {
    font-size: 14px; color: var(--sky); letter-spacing: .5px;
    border-bottom: 1px solid var(--sky); width: 260px; padding-bottom: 2px; margin-top: 2px;
  }
  .company { position: absolute; right: 30px; top: 146px; text-align: right; font-size: 13px; color: var(--ink); line-height: 1.35; }
  .company__name { font-weight: 700; color: var(--sky); font-size: 14px; }
  .contacts { position: absolute; left: 30px; top: 208px; list-style: none; font-size: 14px; color: var(--ink); }
  .contacts li { display: flex; align-items: center; gap: 8px; height: 21px; }
  .contacts svg { width: 14px; height: 14px; }
  .card__base { position: absolute; left: 0; bottom: 0; width: 540px; height: 310px; }
  .website {
    position: absolute; right: 26px; bottom: 28px;
    color: #fff; font-weight: 700; font-size: 14px; letter-spacing: 3px;
  }
</style>
</head>
<body>

<section class="card card--back" aria-label="Business card back">
  <div class="brand-name">STAFFVEX</div>
  <div class="rule"></div>
  <div class="band">EMPLOYEE ENGAGEMENT BEGINS AT RECRUITMENT</div>
</section>

<section class="card card--front" aria-label="Business card front">
  <svg class="card__base" viewBox="0 0 540 310" aria-hidden="true">
    <path d="M0,300 L300,300 C330,300 330,252 362,252 L540,252 L540,310 L0,310 Z" fill="var(--navy)"/>
    <path d="M0,292 L292,292 C318,292 322,246 354,246 L380,246" fill="none" stroke="var(--sky)" stroke-width="5"/>
  </svg>
  <div class="brand-name">STAFFVEX</div>
  <div class="top-rule"></div>

  <div class="person">
    <div class="person__name">MARTIN ELLSWORTH</div>
    <div class="person__role">CO-FOUNDER</div>
  </div>

  <div class="company">
    <div class="company__name">STAFFVEX COMPANY PVT LTD</div>
    <div>42 Harbor Crest Ave</div>
    <div>Fairview, CA</div>
  </div>

  <ul class="contacts">
    <li>
      <svg viewBox="0 0 14 14" aria-hidden="true"><circle cx="7" cy="7" r="7" fill="var(--sky)"/><path d="M4,4.5 Q4,10 9.5,10 L10,8.6 L8.5,8 L7.8,8.7 Q5.6,7.8 5.3,6.2 L6,5.5 L5.4,4 Z" fill="#fff"/></svg>
      +44 207 555 0148
    </li>
    <li>
      <svg viewBox="0 0 14 14" aria-hidden="true"><circle cx="7" cy="7" r="7" fill="var(--sky)"/><rect x="5" y="3" width="4" height="8" rx="1" fill="#fff"/></svg>
      07700 900418
    </li>
    <li>
      <svg viewBox="0 0 14 14" aria-hidden="true"><circle cx="7" cy="7" r="7" fill="var(--sky)"/><rect x="3.5" y="4.5" width="7" height="5" fill="#fff"/><path d="M3.5,4.5 L7,7.5 L10.5,4.5" fill="none" stroke="var(--sky)" stroke-width=".8"/></svg>
      martin.ellsworth@staffvex.com
    </li>
  </ul>

  <div class="website">www.staffvex.com</div>
</section>

</body>
</html>
```